Rollup Banner & Flyer für eine Messe "Erfolg durch Innovation"

Wir benötigten für eine Messe einen Roll Up Banner und Flyer zum verteilen. Gerne basierend auf der aktuellen Firmenpräsentation und mit unseren Referenzen.
Im flyer sollen unserer Leistungen (Datenanalyse, Simulation, Optimierung und Webapplikation) dargestellt werden mit einem kleinen Text und einem aussagekräftigen bild. (https://www.kalvento.ch/leistungen/)

Target Market(s)

Industrie

Industry/Entity Type

Simulation

Font styles to use
Sans Serif
Other font styles liked:
• Roboto

Requirements
Must have
• Logo, Referenzen

```html
<!DOCTYPE html>
<html lang="de">
<head>
<meta charset="utf-8">
<title>Kalvento – Flyer & Roll-up</title>
<link href="https://fonts.googleapis.com/css2?family=Poppins:wght@400;500;600;700;800&display=swap" rel="stylesheet">
<style>
  :root{
    --lime:#dfe06a;
    --ink:#151515;
    --white:#ffffff;
    --stage:#707070;
    --rule:#8a8a8a;
  }
  *{box-sizing:border-box;margin:0;padding:0}
  html,body{width:1200px;height:2783px;overflow:hidden}
  body{background:var(--stage);font-family:'Poppins',sans-serif;color:var(--ink);position:relative}

  .flyer,.rollup{position:absolute;transform-origin:0 0;transform:scale(1.0801);overflow:hidden;background:var(--lime)}
  .flyer{left:104px;top:102px;width:918px;height:1188px}
  .rollup{left:310px;top:1457px;width:537px;height:1139px}
  .abs{position:absolute}

  /* hero */
  .hero{position:absolute;left:0;top:0;width:100%;background:linear-gradient(180deg,#1e1e1e,#0c0c0c 70%,#141414)}
  .brand{position:absolute;display:flex;align-items:center;gap:10px}
  .brand-dot{width:50px;height:50px;border-radius:50%;border:5px solid var(--lime)}
  .brand-name{font-weight:700;font-size:40px;color:var(--white);letter-spacing:1px}
  .headline{position:absolute;color:var(--white)}
  .headline .lead{font-weight:500;font-size:27px;line-height:30px}
  .headline .big{font-weight:800;font-size:45px;line-height:43px;color:var(--lime);letter-spacing:1px}
  .headline p{font-size:14.5px;line-height:16.2px;margin-top:10px}

  /* hero ring visual */
  .ring{position:absolute}
  .ring .photo{position:absolute;border-radius:50%;background:radial-gradient(circle at 45% 40%,#dcdcdc,#a9a9a6 55%,#6e6e6a)}

  /* flyer content */
  .panel{position:absolute;left:59px;top:363px;width:802px;height:741px;background:var(--white);border-radius:0 0 26px 26px}
  .svc{position:absolute}
  .svc h2{font-weight:700;font-size:29px;line-height:32px}
  .svc p{font-size:14.3px;line-height:16.3px;margin-top:6px}
  .pills{display:flex;gap:12px;margin-top:14px}
  .pill{display:flex;align-items:center;gap:4px;width:121px;height:25px;padding-left:12px;background:var(--lime);border-radius:12px;font-size:14px}
  .pill::before{content:"";width:7px;height:7px;border-radius:50%;background:var(--ink);box-shadow:0 0 0 1px var(--ink)}
  .marker{position:absolute;width:18px;height:18px;border-radius:50%;border:3px solid var(--lime);background:var(--white)}
  .line{position:absolute;background:var(--rule)}
  .screen{position:absolute;border-radius:6px;background:linear-gradient(180deg,#2a2a2a 0 4%,#f1f1f1 4% 76%,#d7d7d7 76% 82%,transparent 82%)}
  .screen::after{content:"";position:absolute;left:38%;bottom:0;width:24%;height:16%;background:linear-gradient(180deg,#cfcfcf,#9e9e9e);border-radius:0 0 40% 40%}

  .contact{position:absolute;left:62px;top:1124px;display:flex;gap:28px;font-size:18px;color:var(--ink)}
  .contact span{display:flex;align-items:center;gap:7px}
  .contact svg{width:16px;height:16px}

  /* rollup */
  .r-panel{position:absolute;left:40px;top:535px;width:457px;height:513px;background:var(--white);border-radius:0 0 30px 30px}
  .r-item{position:absolute;left:98px;display:flex;align-items:center;gap:14px}
  .r-icon{width:46px;height:46px;border-radius:50%;background:var(--lime);border:3px solid var(--white);box-shadow:0 0 0 2px var(--ink);display:flex;align-items:center;justify-content:center}
  .r-icon svg{width:22px;height:22px}
  .r-item h3{font-weight:700;font-size:28px}
  .r-rule{position:absolute;left:158px;width:290px;height:2px;background:var(--rule)}
  .r-call{position:absolute;left:92px;top:991px;width:353px;height:57px;background:var(--ink);border-radius:28px 28px 0 0;color:var(--white);display:flex;align-items:center;justify-content:center;gap:14px;font-weight:600;font-size:29px}
  .r-web{position:absolute;left:0;width:100%;top:1056px;text-align:center;font-size:30px;letter-spacing:3px;font-weight:400}
  .r-web b{font-weight:700}
</style>
</head>
<body>

<!-- FLYER -->
<section class="flyer">
  <div class="hero" style="height:363px" role="img" aria-label="Abgedunkeltes Foto einer Seminarrunde im Hintergrund"></div>

  <div class="brand" style="left:52px;top:57px">
    <div class="brand-dot"></div>
    <div class="brand-name">Kalvento</div>
  </div>

  <div class="headline" style="left:57px;top:145px;width:400px">
    <div class="lead">DU HAST EINE SCHWIERIGE</div>
    <div class="big">ENTSCHEIDUNG<br>ZU TREFFEN?</div>
    <p>Was wäre, wenn wir dir zeigen würden, welche Option die Beste ist? Wir unterstützen Unternehmen in Logistik und Produktion die besten Entscheidungen zu treffen und dass nnerhalb weniger Wochen.</p>
  </div>

  <div class="panel"></div>

  <svg class="ring" style="left:488px;top:30px" width="370" height="360" viewBox="0 0 370 360">
    <circle cx="180" cy="172" r="172" fill="#fff"/>
    <circle cx="182" cy="170" r="165" fill="var(--lime)"/>
    <circle cx="198" cy="195" r="153" fill="var(--ink)"/>
    <circle cx="180" cy="165" r="145" fill="#fff"/>
  </svg>
  <div class="ring" style="left:528px;top:75px;width:280px;height:280px">
    <div class="photo" style="inset:0" role="img" aria-label="Foto: Hände an einer Tastatur vor einem Monitor mit Diagrammen"></div>
  </div>

  <!-- Datenanalyse -->
  <div class="marker" style="left:82px;top:393px"></div>
  <div class="line" style="left:90px;top:411px;width:2px;height:132px"></div>
  <div class="line" style="left:90px;top:542px;width:570px;height:2px"></div>
  <div class="svc" style="left:131px;top:385px;width:480px">
    <h2>Datenanalyse</h2>
    <p>Datenanalyse macht Prozesse sichtbar, erkennt Muster und schafft eine objektive Grundlage für Entscheidungen. Wir strukturieren, bereinigen und analysieren Daten so, dass sie einen echten Nutzen erzeugen.</p>
    <div class="pills"><span class="pill">Transparent</span><span class="pill">Verständlich</span><span class="pill">Aussagekräftig</span></div>
  </div>
  <div class="screen" style="left:650px;top:385px;width:178px;height:180px" role="img" aria-label="Monitor mit Dashboard zur Datenanalyse"></div>

  <!-- Simulation -->
  <div class="screen" style="left:88px;top:552px;width:178px;height:182px" role="img" aria-label="Monitor mit Karte eines Routenplaners"></div>
  <div class="marker" style="left:810px;top:579px"></div>
  <div class="line" style="left:818px;top:597px;width:2px;height:128px"></div>
  <div class="line" style="left:250px;top:724px;width:570px;height:2px"></div>
  <div class="svc" style="left:333px;top:571px;width:400px">
    <h2>Simulation</h2>
    <p>Simulation bildet reale Prozesse digital ab, damit Abläufe, Kapazitäten und Varianten risikofrei getestet werden können.</p>
    <div class="pills"><span class="pill">Vergleichbar</span><span class="pill">Belastbar</span><span class="pill">Risikoarm</span></div>
  </div>

  <!-- Optimierung -->
  <div class="marker" style="left:82px;top:747px"></div>
  <div class="line" style="left:90px;top:765px;width:2px;height:132px"></div>
  <div class="line" style="left:90px;top:896px;width:570px;height:2px"></div>
  <div class="svc" style="left:131px;top:743px;width:480px">
    <h2>Optimierung</h2>
    <p>Optimierung sucht automatisch nach der besten Lösung – sei es bei Planung, Ressourcen, Routen oder Abläufen. Mit Algorithmen und intelligenten Modellen finden wir Varianten, die Kosten senken, Kapazitäten besser nutzen und Entscheidungen beschleunigen.</p>
    <div class="pills"><span class="pill">Effizient</span><span class="pill">Zielgerichtet</span><span class="pill">Robust</span></div>
  </div>
  <div class="screen" style="left:650px;top:738px;width:178px;height:182px" role="img" aria-label="Monitor mit Planungs-Gantt-Ansicht"></div>

  <!-- Webapplikationen -->
  <div class="screen" style="left:88px;top:910px;width:178px;height:184px" role="img" aria-label="Monitor mit Webapplikation und Balkendiagramm"></div>
  <div class="marker" style="left:810px;top:934px"></div>
  <div class="line" style="left:818px;top:952px;width:2px;height:128px"></div>
  <div class="line" style="left:250px;top:1079px;width:570px;height:2px"></div>
  <div class="svc" style="left:333px;top:926px;width:450px">
    <h2>Webapplikationen</h2>
    <p>Wir entwickeln individuelle Webapplikationen, die Daten, Simulationen und Optimierungen in einem benutzerfreundlichen Tool zusammenführen. So entstehen Lösungen, die direkt im Alltag genutzt werden – einfach, schnell und ohne Installation.</p>
    <div class="pills"><span class="pill">Zugänglich</span><span class="pill">Verfügbar</span><span class="pill">Flexibe</span></div>
  </div>

  <div class="contact">
    <span><svg viewBox="0 0 24 24"><path d="M6.6 10.8a15 15 0 006.6 6.6l2.2-2.2c.3-.3.7-.4 1-.2 1.1.4 2.3.6 3.6.6.6 0 1 .4 1 1V20c0 .6-.4 1-1 1A17 17 0 013 4c0-.6.4-1 1-1h3.5c.6 0 1 .4 1 1 0 1.3.2 2.5.6 3.6.1.3 0 .7-.2 1z" fill="none" stroke="#151515" stroke-width="2"/></svg>+41 81 000 12 34</span>
    <span><svg viewBox="0 0 24 24"><path d="M2 5h20v14H2z M2 5l10 8 10-8" fill="none" stroke="#151515" stroke-width="2"/></svg>info@kalvento.ch</span>
    <span><svg viewBox="0 0 24 24"><path d="M12 2a7 7 0 00-7 7c0 5 7 13 7 13s7-8 7-13a7 7 0 00-7-7zm0 9.5A2.5 2.5 0 1112 6a2.5 2.5 0 010 5.5z" fill="#151515"/></svg>Feldstrasse 14, 7000 Chur</span>
    <span><svg viewBox="0 0 24 24"><circle cx="12" cy="12" r="10" fill="none" stroke="#151515" stroke-width="2"/><path d="M2 12h20M12 2c3 3 3 17 0 20M12 2c-3 3-3 17 0 20" fill="none" stroke="#151515" stroke-width="1.6"/></svg>www.kalvento.ch</span>
  </div>
</section>

<!-- ROLL-UP -->
<section class="rollup">
  <div class="hero" style="height:535px" role="img" aria-label="Abgedunkeltes Foto einer Seminarrunde im Hintergrund"></div>

  <div class="brand" style="left:140px;top:44px">
    <div class="brand-dot"></div>
    <div class="brand-name">Kalvento</div>
  </div>

  <div class="headline" style="left:0;top:116px;width:100%;text-align:center">
    <div class="lead">DU HAST EINE SCHWIERIGE</div>
    <div class="big">ENTSCHEIDUNG<br>ZU TREFFEN?</div>
    <p style="padding:0 70px;font-size:14px;line-height:16px">Was wäre, wenn wir dir zeigen würden, welche Option die Beste ist? Wir unterstützen Unternehmen in Logistik und Produktion die besten Entscheidungen zu treffen und dass nnerhalb weniger Wochen.</p>
  </div>

  <div class="r-panel"></div>

  <svg class="ring" style="left:72px;top:338px" width="400" height="380" viewBox="0 0 400 380">
    <circle cx="195" cy="190" r="188" fill="#fff"/>
    <circle cx="196" cy="186" r="182" fill="var(--lime)"/>
    <circle cx="214" cy="212" r="166" fill="var(--ink)"/>
    <circle cx="193" cy="180" r="160" fill="#fff"/>
  </svg>
  <div class="ring" style="left:109px;top:362px;width:312px;height:312px">
    <div class="photo" style="inset:0" role="img" aria-label="Foto: Hände an einer Tastatur vor einem Monitor mit Diagrammen"></div>
  </div>

  <div class="r-item" style="top:732px">
    <div class="r-icon"><svg viewBox="0 0 24 24"><path d="M4 20V13M9 20V9M14 20V11M19 20V5" stroke="#151515" stroke-width="3"/></svg></div>
    <h3>Datenanalyse</h3>
  </div>
  <div class="r-rule" style="top:786px"></div>
  <div class="r-item" style="top:797px">
    <div class="r-icon"><svg viewBox="0 0 24 24"><circle cx="12" cy="12" r="9" fill="#151515"/><path d="M7 9l4 2 2 5 3-6" stroke="#dfe06a" stroke-width="1.8" fill="none"/></svg></div>
    <h3>Simulation</h3>
  </div>
  <div class="r-rule" style="top:851px"></div>
  <div class="r-item" style="top:859px">
    <div class="r-icon"><svg viewBox="0 0 24 24"><circle cx="12" cy="12" r="8" fill="none" stroke="#151515" stroke-width="3" stroke-dasharray="4 2.3"/><circle cx="12" cy="12" r="3.5" fill="#151515"/></svg></div>
    <h3>Optimierung</h3>
  </div>
  <div class="r-rule" style="top:917px"></div>
  <div class="r-item" style="top:925px">
    <div class="r-icon"><svg viewBox="0 0 24 24"><rect x="3" y="4" width="18" height="15" rx="2" fill="#151515"/><rect x="5" y="8" width="14" height="9" fill="#dfe06a"/></svg></div>
    <h3>Webapplikationen</h3>
  </div>

  <div class="r-call">
    <svg width="26" height="26" viewBox="0 0 24 24"><path d="M6.6 10.8a15 15 0 006.6 6.6l2.2-2.2c.3-.3.7-.4 1-.2 1.1.4 2.3.6 3.6.6.6 0 1 .4 1 1V20c0 .6-.4 1-1 1A17 17 0 013 4c0-.6.4-1 1-1h3.5c.6 0 1 .4 1 1 0 1.3.2 2.5.6 3.6.1.3 0 .7-.2 1z" fill="none" stroke="#dfe06a" stroke-width="2"/></svg>
    +41 81 000 12 34
  </div>
  <div class="r-web">www.<b>kalvento</b>.ch</div>
</section>

</body>
</html>
```